Eco retreat in Coralvane Shoals

Would like a web design for letting this holiday property. It is available on lodjo see https://www.lodjo.com.au/accommodation/qld/palmcrest/tern-cove/57203
and NestRoo https://www.nestroo.com.au/rooms/6120957
I also want it to have its' own website for bookings with a calendar and email inquiry. Can use images and wording from lodjo or Nest Roo sites.
The existing facility is the main house with plans for expansion with eco-treehouses and beach chalets. So can you sue picture of the bedrooms and lounges. The colours are amazing.
Updates

Project Deadline Extended
Reason: My apologies but I have been doing landscaping up on the property and wanted to provide additional images. I will attach these to the brief.

Target Market(s)

Is middle to upper income people who love nature, quietness, exercise

Industry/Entity Type

Accommodation

Coding

Coded - Design and coding required

Number of Pages Required

3 page

Font styles to use
Sans Serif

Colors
33b8a4
ffc214
0692cd

Requirements
Must have
• Main page that provides the overall ambience and ability to book quickly
• 2 nd page with the activities (diving, riding) and house facilities (pictures of the rooms and lounges)
• 3 rd page would be the location and logistics of getting there
Nice to have
• Simplicity through images and key phrases that invites connection
Should not have
• too much text

```html
<!DOCTYPE html>
<html lang="en">
<head>
<meta charset="utf-8">
<title>Kalinda – holiday letting property</title>
<link href="https://fonts.googleapis.com/css2?family=Arvo:wght@400;700&family=Open+Sans:wght@300;400;600;700&family=Raleway:wght@300&display=swap" rel="stylesheet">
<style>
:root{
  --green:#8cb82b;
  --green-dark:#7aa322;
  --orange:#f7941d;
  --ink:#2b2b2b;
  --text:#555;
  --muted:#888;
  --topbar:#262626;
  --footer:#2f2f2f;
  --footer-bottom:#262626;
  --white:#fff;
  --line:#d6d6d6;
}
*{box-sizing:border-box;margin:0;padding:0}
html,body{width:1200px;height:3982px;overflow:hidden}
body{font-family:"Open Sans",Arial,sans-serif;color:var(--text);background:var(--white);font-size:13px;line-height:1.7}
.heading{font-family:"Arvo",Georgia,serif;font-weight:400;color:var(--ink);text-align:center;letter-spacing:1px}

/* top bar */
.topbar{height:32px;background:var(--topbar);color:#ddd;font-size:11px;display:flex;align-items:center;justify-content:space-between;padding:0 100px}
.topbar .contact span{margin-right:26px;display:inline-flex;align-items:center;gap:6px}
.topbar .social{display:flex;align-items:center;gap:12px}
.topbar .social i{width:10px;height:10px;border-radius:2px;background:var(--green);display:inline-block}
.dot{width:9px;height:9px;border-radius:50%;background:var(--green);display:inline-block}

/* header */
.site-header{height:101px;display:flex;align-items:center;justify-content:space-between;padding:0 100px}
.brand{display:flex;align-items:center;gap:12px}
.brand-mark{width:46px;height:46px;border-radius:50%;background:var(--green)}
.brand-name{font-family:"Arvo",Georgia,serif;font-size:22px;color:var(--green-dark)}
.main-nav{display:flex;gap:46px;font-size:12px;letter-spacing:1px;color:#444;text-transform:uppercase}

/* hero */
.hero{position:relative;height:563px;background:linear-gradient(180deg,#5d8fb8 0%,#9ec2d6 28%,#3f6e4d 48%,#7a4d2e 60%,#4c7a2c 82%,#5f9a2d 100%)}
.hero-title{position:absolute;left:600px;top:232px;color:var(--white);font-family:"Raleway",sans-serif;font-weight:300;line-height:1}
.hero-title .name{font-size:64px;display:block}
.hero-title .tag{font-size:42px;display:block;margin-top:6px}

.booking{position:absolute;left:165px;top:412px;width:868px;height:178px;background:var(--white);box-shadow:0 14px 26px rgba(0,0,0,.18);padding:20px 30px}
.booking h2{font-family:"Arvo",Georgia,serif;font-weight:400;font-size:21px;color:var(--ink);letter-spacing:1px;margin-bottom:16px}
.booking .fields{display:flex;gap:12px}
.booking .field{flex:1;height:26px;border:1px solid #c9c9c9;font-size:10px;color:#777;display:flex;align-items:center;justify-content:space-between;padding:0 6px;text-transform:uppercase}
.booking .field b{width:11px;height:11px;border:1px solid #999;display:inline-block}
.booking .actions{display:flex;align-items:center;gap:22px;margin-top:14px}
.btn-orange{background:var(--orange);color:var(--white);font-size:12px;font-weight:600;width:196px;height:40px;display:flex;align-items:center;justify-content:center;text-transform:uppercase}
.booking .actions p{font-style:italic;font-size:13px;color:#444}

/* welcome */
.welcome{padding-top:108px;height:540px}
.welcome h2{font-size:35px}
.welcome .lead{width:890px;margin:28px auto 0;text-align:center;font-size:13px;line-height:2}
.features{display:flex;justify-content:center;gap:60px;margin-top:46px}
.feature{width:300px;display:flex;gap:24px}
.feature .icon{flex:none;width:66px;height:66px;border-radius:50%;background:var(--green);display:flex;align-items:center;justify-content:center}
.feature h3{font-family:"Arvo",Georgia,serif;font-weight:400;font-size:17px;color:var(--ink);margin-bottom:4px}
.feature p{font-size:12px;line-height:1.9}

/* tree */
.tree-intro{height:232px;padding-top:0}
.tree-intro h2{font-size:34px;padding-top:0}
.tree-intro p{text-align:center;font-size:13px;margin-top:10px}
.tree-grid{display:grid;grid-template-columns:repeat(4,300px);grid-auto-rows:237px}
.tile-photo{display:block}
.tile-text{background:var(--green);color:var(--white);text-align:center;padding:30px 32px 0}
.tile-text h3{font-family:"Arvo",Georgia,serif;font-weight:400;font-size:19px;margin-bottom:10px}
.tile-text p{font-size:12px;line-height:1.9}
.btn-outline{display:inline-block;margin-top:16px;border:1px solid var(--white);font-size:12px;padding:6px 26px}

/* events */
.events{padding-top:78px;height:558px}
.events h2{font-size:33px}
.events .lead{width:900px;margin:20px auto 0;text-align:center;line-height:2}
.event-list{display:flex;gap:8px;margin:38px 0 0 98px}
.event{width:244px;text-align:center}
.event .photo{height:194px}
.event h3{font-family:"Arvo",Georgia,serif;font-weight:400;font-size:17px;color:var(--ink);margin-top:20px}
.event time{font-size:12px;color:#666}

/* spa */
.spa{height:430px;background:linear-gradient(100deg,#5a3b2a 0%,#a47458 35%,#c79a7c 60%,#6a4a38 100%);color:var(--white);text-align:center;padding-top:118px}
.spa h2{color:var(--white);font-size:34px}
.spa p{width:860px;margin:14px auto 0;font-size:13px;line-height:2}
.btn-green{display:inline-block;background:var(--green);color:var(--white);font-size:14px;padding:13px 32px;margin-top:26px}

/* inquiry */
.inquiry{height:380px;padding-top:92px}
.inquiry h2{font-size:33px}
.inquiry p{width:900px;margin:18px auto 0;text-align:center;line-height:2}
.subscribe{display:flex;justify-content:center;gap:14px;margin-top:36px}
.subscribe .input{width:436px;height:43px;border:1px solid var(--line);font-size:12px;color:#777;display:flex;align-items:center;padding:0 12px}
.subscribe .btn{width:204px;height:43px;background:var(--green);color:var(--white);font-size:14px;font-weight:600;letter-spacing:1px;display:flex;align-items:center;justify-content:center}

/* testimonial */
.testimonial{height:462px;background:linear-gradient(180deg,#3b3029 0%,#6b5343 40%,#8c6a4e 62%,#3b2f27 100%);color:var(--white);text-align:center;padding-top:122px}
.testimonial .quote{font-family:"Arvo",Georgia,serif;font-size:40px;color:var(--green);line-height:1}
.testimonial p{width:820px;margin:14px auto 0;font-size:13px;line-height:2}
.avatar{width:100px;height:100px;border-radius:50%;background:#c9b8a6;border:4px solid var(--green);margin:26px auto 0}
.author{margin-top:18px;font-size:13px}
.author b{font-weight:700}

/* footer */
.site-footer{height:339px;background:var(--footer);color:#bbb;position:relative}
.footer-inner{display:flex;padding:40px 0 0 100px}
.footer-brand{font-family:"Arvo",Georgia,serif;color:var(--green);font-size:32px;position:absolute;left:100px;top:34px}
.footer-links{margin-top:62px;width:258px;font-size:11px;line-height:2.6}
.footer-links.narrow{width:210px}
.connect{position:absolute;left:770px;top:36px}
.connect .circles{display:flex;gap:8px}
.connect .circles i{width:24px;height:24px;border-radius:50%;background:var(--white);display:block}
.connect h3{font-family:"Open Sans",sans-serif;font-weight:600;color:var(--white);font-size:17px;letter-spacing:1px;margin-top:34px}
.connect .signup{display:flex;margin-top:14px}
.connect .signup .input{width:246px;height:36px;background:#222;color:#888;font-size:11px;display:flex;align-items:center;padding:0 10px}
.connect .signup .btn{width:94px;height:36px;background:var(--green);color:var(--white);font-size:12px;font-weight:600;display:flex;align-items:center;justify-content:center;margin-left:8px}
.connect ul{list-style:none;margin-top:16px;font-size:11px;line-height:2.4}
.connect li{display:flex;align-items:center;gap:8px}
.footer-bottom{position:absolute;left:0;right:0;bottom:0;height:38px;background:var(--footer-bottom);font-size:11px;color:#888;display:flex;align-items:center;justify-content:center}
</style>
</head>
<body>

<div class="topbar">
  <div class="contact">
    <span><i class="dot"></i>Call Us : 4817 | 302 559</span>
    <span><i class="dot"></i>Email Us : hello@kalinda.com</span>
  </div>
  <div class="social">Connect with our social network : <i></i><i></i><i></i><i></i><i></i></div>
</div>

<header class="site-header">
  <div class="brand"><span class="brand-mark"></span><span class="brand-name">the Kalinda Tree</span></div>
  <nav class="main-nav"><span>Home</span><span>Location</span><span>Reviews</span><span>Features</span><span>Prices</span><span>Contact Us</span></nav>
</header>

<section class="hero" role="img" aria-label="Resort houses with a pool beside palm trees and the ocean">
  <h1 class="hero-title"><span class="name">Kalinda</span><span class="tag">holiday letting property</span></h1>
  <form class="booking">
    <h2>BOOKING YOUR FAVORITE</h2>
    <div class="fields">
      <div class="field">Location<b></b></div>
      <div class="field">Adults<b></b></div>
      <div class="field">Check In<b></b></div>
      <div class="field">Check Out<b></b></div>
    </div>
    <div class="actions">
      <div class="btn-orange">Check Availability</div>
      <p>Lorem Ipsum is simply dummy text of the printing and typesetting industry.</p>
    </div>
  </form>
</section>

<section class="welcome">
  <h2 class="heading">WELCOME TO KALINDA</h2>
  <p class="lead">Enjoying absolute beachfront flanked by bushland, the exotic furnishings and art showcase the Pacific Island cultures of New Guinea and Fiji. The tranquility and astounding natural beauty of this tropical paradise make it the perfect setting for relaxation, a special celebration or just a chance to getaway from the hectic pace or the everyday grind.</p>
  <div class="features">
    <div class="feature">
      <div class="icon"><svg width="28" height="32" viewBox="0 0 28 32"><path d="M14 2a10 10 0 0 0-10 10c0 8 10 18 10 18s10-10 10-18A10 10 0 0 0 14 2z" fill="none" stroke="#fff" stroke-width="2.4"/><circle cx="14" cy="12" r="3.6" fill="#fff"/></svg></div>
      <div><h3>Location</h3><p>Lorem Ipsum is simply dummy text of the printing and typesetting industry. has been the industry's standard dummy...</p></div>
    </div>
    <div class="feature">
      <div class="icon"><svg width="28" height="30" viewBox="0 0 28 30"><path d="M10 23V5l14-3v18" fill="none" stroke="#fff" stroke-width="2.4"/><circle cx="6.5" cy="23.5" r="4" fill="none" stroke="#fff" stroke-width="2.4"/><circle cx="20.5" cy="20.5" r="4" fill="none" stroke="#fff" stroke-width="2.4"/></svg></div>
      <div><h3>Activities</h3><p>Lorem Ipsum is simply dummy text of the printing and typesetting industry. has been the industry's standard dummy...</p></div>
    </div>
    <div class="feature">
      <div class="icon"><svg width="30" height="30" viewBox="0 0 30 30"><rect x="3" y="5" width="24" height="22" rx="2" fill="none" stroke="#fff" stroke-width="2.4"/><path d="M3 11h24M9 2v6M21 2v6" stroke="#fff" stroke-width="2.4"/><path d="M8 16h3M14 16h3M20 16h3M8 21h3M14 21h3" stroke="#fff" stroke-width="2.4"/></svg></div>
      <div><h3>Events</h3><p>Lorem Ipsum is simply dummy text of the printing and typesetting industry. has been the industry's standard dummy...</p></div>
    </div>
  </div>
</section>

<section class="tree-intro">
  <h2 class="heading">THE KALINDA TREE</h2>
  <p>Coralvane Shoals Eco-retreat and Wellness Centre</p>
</section>
<div class="tree-grid">
  <div class="tile-photo" role="img" aria-label="Main house lit at dusk beside the pool" style="background:linear-gradient(160deg,#3a2a1e,#b8874e 55%,#5fa5b8)"></div>
  <div class="tile-text"><h3>The Eco-retreat</h3><p>Designed by a renowned tropics architect the Pacific Island influenced main house features large wrap...</p><span class="btn-outline">Click here</span></div>
  <div class="tile-photo" role="img" aria-label="Overwater bungalows above a turquoise lagoon" style="background:linear-gradient(180deg,#5aa7d8,#9fd0e6 45%,#6b4a2e 60%,#1fa3c9)"></div>
  <div class="tile-text"><h3>The Tented treehouses</h3><p>Designed by a renowned tropics architect the Pacific Island influenced main house features large wrap...</p><span class="btn-outline">Click here</span></div>
  <div class="tile-text"><h3>The Main house</h3><p>Designed by a renowned tropics architect the Pacific Island influenced main house features large wrap...</p><span class="btn-outline">Click here</span></div>
  <div class="tile-photo" role="img" aria-label="Timber beach house among trees" style="background:linear-gradient(170deg,#5c6a54,#6d4b34 50%,#3c3a2a)"></div>
  <div class="tile-text"><h3>The Beach houses</h3><p>Designed by a renowned tropics architect the Pacific Island influenced main house features large wrap...</p><span class="btn-outline">Click here</span></div>
  <div class="tile-photo" role="img" aria-label="Tented treehouse bedroom with white bed" style="background:linear-gradient(170deg,#6a5a3c,#b7a783 50%,#4a3d2a)"></div>
</div>

<section class="events">
  <h2 class="heading">SPECIAL EVENTS - WEDDINGS+ EVENTS</h2>
  <p class="lead">Kalinda Tree is the perfect setting for small weddings and events. These can be held on the beach or on the extensive grounds, at the Main House or for something truly unique, out under the stars.</p>
  <div class="event-list">
    <article class="event"><div class="photo" role="img" aria-label="Cyclists riding past green hills" style="background:linear-gradient(180deg,#6fa0d6,#8fb86a 55%,#5c7a3a)"></div><h3>Lorem Ipsum is simply</h3><time>On 24 March 2016</time></article>
    <article class="event"><div class="photo" role="img" aria-label="Couple doing yoga on the beach" style="background:linear-gradient(180deg,#8ec3e8,#e8eef2 55%,#d9c9a8)"></div><h3>Lorem Ipsum is simply</h3><time>On 24 March 2016</time></article>
    <article class="event"><div class="photo" role="img" aria-label="Party crowd under coloured lights" style="background:linear-gradient(160deg,#1e1a3a,#6a2a6a 50%,#d08a3a)"></div><h3>Lorem Ipsum is simply</h3><time>On 24 March 2016</time></article>
    <article class="event"><div class="photo" role="img" aria-label="Friends celebrating with drinks at night" style="background:linear-gradient(160deg,#2a1a12,#b0552a 50%,#e6a04a)"></div><h3>Lorem Ipsum is simply</h3><time>On 24 March 2016</time></article>
  </div>
</section>

<section class="spa" role="img" aria-label="Massage treatment in a spa">
  <h2 class="heading">SPA AND TREATMENTS</h2>
  <p>Kalinda Tree offers a range of day spa and special treatments which can be enjoyed in the privacy of your own chalet or in the Main House. These include detoxifying, relaxing, energising and balancing treatments with a focus around organic products.</p>
  <span class="btn-green">View more info</span>
</section>

<section class="inquiry">
  <h2 class="heading">EMAIL INQUIRY</h2>
  <p>Lorem Ipsum is simply dummy text of the printing and typesetting industry. Lorem Ipsum has been the industry's standard dummy text ever since the 1500s, when an unknown printer took a galley of type and scrambled</p>
  <div class="subscribe"><div class="input">Enter your email id</div><div class="btn">SUBSCRIBE</div></div>
</section>

<section class="testimonial" role="img" aria-label="Family running along the beach at sunset">
  <div class="quote">&ldquo;</div>
  <p>Lorem Ipsum is simply dummy text of the printing and typesetting industry. Lorem Ipsum has been the industry's standard dummy text ever since the 1500s, when an unknown printer took a galley of type and scrambled it to make a type specimen book</p>
  <div class="avatar" role="img" aria-label="Guest portrait"></div>
  <div class="author">- <b>Marcus Ellory</b> - Business man</div>
</section>

<footer class="site-footer">
  <div class="footer-brand">Kalinda</div>
  <div class="footer-inner">
    <div class="footer-links">Accommodation<br>Last Minute Accommodation<br>Phillip Island Accommodation<br>Lorne Accommodation<br>Sunshine Coast Accommodation</div>
    <div class="footer-links">Sydney Accommodation<br>Melbourne Accommodation<br>Gold Coast Accommodation<br>Byron Bay Accommodation<br>Noosa Accommodation</div>
    <div class="footer-links narrow">Travel Extras<br>Travel Ideas<br>School &amp; public holiday<br>Wayfarer Guide<br>Media Centre</div>
  </div>
  <div class="connect">
    <div class="circles"><i></i><i></i><i></i><i></i><i></i></div>
    <h3>STAY CONNECTED</h3>
    <div class="signup"><div class="input">Enter your email id</div><div class="btn">SIGNUP</div></div>
    <ul>
      <li><i class="dot"></i>4817 | 302 559</li>
      <li><i class="dot"></i>hello@kalinda.com</li>
    </ul>
  </div>
  <div class="footer-bottom">Copyright © 2016, Kalinda. All rights reserved.</div>
</footer>

</body>
</html>
```